Tradeline Summit & Expo xmas banner/MREC promotion

Size:
• Leader board: 728 x 90 px
• MREC: 300 x250 px
• Half-page: 300 x 600
• Wide skyscraper: 160 x 600
Image:
Candy cane stripes as the background – image bought. Horizontal or vertical whatever you think will works.
White strip/background for the copy? See images example – unless you don’t need to do that?
Bold font which is "neutra" to our other banners attached. I think black font would look good.
Message:
Please give it a good readable pace between slides – 3 secs?
1st Slide
It’s silly season!
2nd Slide
Treat yourself to an end of year gift
3rd Slide
Book your ticket now and save $$$
4th Slide
Get spoilt. You’re worth it!
5th Slide
Tradeline logo
Target Market(s)
anyone that sells online
• Automotive • Advertising • Digital • Entertainment
• Finance • Hospitality • Pharmaceutical/Healthcare • Pop Culture
• Retail • Travel • Telecommunications

```html
<!DOCTYPE html>
<html lang="en">
<head>
<meta charset="UTF-8">
<title>It's Silly Season – Holiday Banner</title>
<link rel="stylesheet" href="https://fonts.googleapis.com/css2?family=League+Spartan:wght@800&display=swap">
<style>
  :root {
    --candy-red: #c8102e;
    --candy-red-deep: #9e0b22;
    --candy-white: #f4eeee;
    --frost-white: #ffffff;
    --ink: #0d0d0d;
  }
  html, body {
    margin: 0;
    padding: 0;
    width: 1200px;
    height: 2400px;
    overflow: hidden;
    background: var(--candy-white);
  }
  .banner {
    position: relative;
    width: 1200px;
    height: 2400px;
    overflow: hidden;
  }
  .candy-backdrop {
    position: absolute;
    inset: 0;
    background:
      linear-gradient(180deg,
        var(--candy-red) 0%,
        var(--candy-white) 18%,
        var(--candy-red) 36%,
        var(--candy-white) 54%,
        var(--candy-red) 72%,
        var(--candy-white) 88%,
        var(--candy-red-deep) 100%);
  }
  .frost-panel {
    position: absolute;
    left: 20px;
    top: 730px;
    width: 1160px;
    height: 960px;
    border-radius: 50%;
    background: radial-gradient(ellipse at center,
      var(--frost-white) 0%,
      var(--frost-white) 60%,
      rgba(255,255,255,0.85) 68%,
      rgba(255,255,255,0) 72%);
  }
  .headline {
    position: absolute;
    left: 0;
    right: 0;
    top: 915px;
    margin: 0;
    text-align: center;
    font-family: "League Spartan", "Montserrat", sans-serif;
    font-weight: 800;
    font-size: 192px;
    line-height: 184px;
    letter-spacing: 2px;
    color: var(--ink);
    text-transform: uppercase;
  }
</style>
</head>
<body>
  <div class="banner">
    <div class="candy-backdrop" role="img" aria-label="Photograph of red and white striped candy canes laid horizontally"></div>
    <div class="frost-panel" role="img" aria-label="Frosty white snowflake edged panel behind the message"></div>
    <h1 class="headline">It’s<br>Silly<br>Season!</h1>
  </div>
</body>
</html>
```